New Business Card Design Project

I would like my card design to look exactly like the logo, design, layout, and print of the current attached file. The only change I would like made would be for the print to say THE KMW GROUP instead of THE HALLORAN GROUP. Basically, just replace his group name with my group name. I would also like the backgroud to be the same texture and color as the attached file. I love the dark blue lettering and house logo on the card.

I am completely open to the rest of the card design. I just want something clean and simple. Only basic contact info required on the card. Maybe just name: Kyle M Warrick and cell # 555.914.2087 and email kyle@orchidhomesagent.com

```html
<!DOCTYPE html>
<html lang="en">
<head>
<meta charset="utf-8">
<title>The KMW Group – Business Card</title>
<link rel="stylesheet" href="https://fonts.googleapis.com/css2?family=Arimo:wght@400;700&display=swap">
<style>
  :root {
    --page-bg: #e9eaec;
    --card-bg: #ffffff;
    --navy: #0f2c5e;
    --name-blue: #123f7a;
    --contact-blue: #1d3f86;
    --mark-ink: #111111;
  }
  * { margin: 0; padding: 0; box-sizing: border-box; }
  html, body {
    width: 1200px;
    height: 800px;
    overflow: hidden;
    background: var(--page-bg);
    font-family: "Arimo", Arial, sans-serif;
  }
  .canvas {
    position: relative;
    width: 1200px;
    height: 800px;
  }
  .business-card {
    position: absolute;
    left: 180px;
    top: 160px;
    width: 840px;
    height: 480px;
    background: var(--card-bg);
    box-shadow: 0 10px 30px rgba(0, 0, 0, 0.18);
    overflow: hidden;
  }
  .roof-band {
    position: absolute;
    inset: 0;
    width: 840px;
    height: 480px;
  }
  .roof-band polygon { fill: var(--navy); }
  .brand-lockup {
    position: absolute;
    left: 0;
    right: 0;
    top: 168px;
    display: flex;
    justify-content: center;
    align-items: center;
    gap: 18px;
  }
  .brand-square {
    width: 62px;
    height: 62px;
    background: var(--mark-ink);
  }
  .brand-name {
    color: var(--mark-ink);
    font-weight: 400;
    font-size: 30px;
    line-height: 1.15;
    letter-spacing: 6px;
    text-transform: uppercase;
  }
  .contact {
    position: absolute;
    left: 0;
    right: 0;
    top: 285px;
    text-align: center;
  }
  .contact-name {
    color: var(--name-blue);
    font-weight: 700;
    font-size: 62px;
    line-height: 1;
    margin-bottom: 22px;
  }
  .contact-line {
    color: var(--contact-blue);
    font-weight: 400;
    font-size: 29px;
    line-height: 1.35;
  }
</style>
</head>
<body>
<main class="canvas">
  <section class="business-card" aria-label="The KMW Group business card">
    <svg class="roof-band" viewBox="0 0 840 480" aria-hidden="true">
      <polygon points="0,0 840,0 840,135 380,42 0,170"/>
    </svg>
    <div class="brand-lockup">
      <span class="brand-square"></span>
      <div class="brand-name">The KMW<br>Group</div>
    </div>
    <div class="contact">
      <p class="contact-name">Kyle M Warrick</p>
      <p class="contact-line">555.914.2087</p>
      <p class="contact-line">kyle@orchidhomesagent.com</p>
    </div>
  </section>
</main>
</body>
</html>
```